RTV Business Card

We need a new design for our business cards. We are brokers in the scrap metal industry and wants something nice, clean and very professional.

Industry/Entity Type

Business

Requirements
Must have
• Our logo
• Would probably be good to incorporate colors from logo into design.
• Example info we need on the cards.
• Name
• Company Address
• Cell Phone
• Office Phone
• Fax
• Email
• Company Website
Should not have
• Should not be too cluttered. Needs to be nice, clean and professional looking.

```html
<!DOCTYPE html>
<html lang="en">
<head>
<meta charset="utf-8">
<title>RTV Metal Trading – Business Card</title>
<link rel="stylesheet" href="https://fonts.googleapis.com/css2?family=Encode+Sans+Condensed:wght@700&family=Questrial&display=swap">
<style>
  :root {
    --ink: #1d1d1f;
    --accent-red: #e2262b;
    --brand-blue: #1b6fb0;
    --brand-navy: #0b3c68;
    --paper: #ffffff;
    --rule: #1f4f8a;
  }
  html, body {
    margin: 0;
    padding: 0;
    width: 1200px;
    height: 702px;
    overflow: hidden;
    background: var(--paper);
  }
  .card {
    position: relative;
    width: 1200px;
    height: 702px;
    background: var(--paper);
    font-family: "Questrial", "Century Gothic", sans-serif;
    color: var(--ink);
    overflow: hidden;
  }
  .brand-mark {
    position: absolute;
    left: 84px;
    top: 84px;
    width: 170px;
    height: 170px;
    background: var(--brand-blue);
  }
  .brand-name {
    position: absolute;
    left: 296px;
    top: 118px;
    margin: 0;
    font-family: "Encode Sans Condensed", "Arial Narrow", sans-serif;
    font-weight: 700;
    font-size: 92px;
    line-height: 1;
    letter-spacing: -1px;
    color: var(--ink);
  }
  .person {
    position: absolute;
    right: 826px;
    top: 338px;
    text-align: right;
  }
  .person-name {
    margin: 0;
    font-size: 30px;
    color: var(--accent-red);
    letter-spacing: 0.5px;
  }
  .person-role {
    margin: 10px 0 0;
    font-size: 28px;
  }
  .divider {
    position: absolute;
    left: 419px;
    top: 345px;
    width: 2px;
    height: 169px;
    background: var(--rule);
  }
  .contact {
    position: absolute;
    right: 85px;
    top: 338px;
    text-align: right;
    font-size: 28px;
    line-height: 38px;
    letter-spacing: 0.4px;
  }
  .contact p { margin: 0; }
  .contact .address { margin-top: 20px; }
  .footer-band {
    position: absolute;
    left: 0;
    top: 558px;
    width: 1200px;
    height: 144px;
    background: var(--brand-navy);
    display: flex;
    align-items: center;
    justify-content: center;
  }
  .website {
    margin: 0 0 0 -6px;
    color: var(--paper);
    font-size: 36px;
    letter-spacing: 2.5px;
  }
</style>
</head>
<body>
  <div class="card">
    <div class="brand-mark" aria-hidden="true"></div>
    <h1 class="brand-name">RTV Metal Trading</h1>

    <div class="person">
      <p class="person-name">Name Surname</p>
      <p class="person-role">CEO / Founder</p>
    </div>

    <div class="divider"></div>

    <div class="contact">
      <p>Phone: (555) 218-7340</p>
      <p>Fax: (555) 218-7341</p>
      <p>(E): info@rtvmetaltrading.com</p>
      <p class="address">742 Foundry Lane, Millbrook, SC 29000</p>
    </div>

    <div class="footer-band">
      <p class="website">www.rtvmetaltrading.com</p>
    </div>
  </div>
</body>
</html>
```